A Hong Kong Veterinary Clinic needs a design for clinic door front signage

We are a veterinary clinic locates in the area of "San Po Kong" in Hong Kong, need a new sign (the wooden section in the photos shown below) above the front glass doors. The old signs are shown on https://www.lmt-petcare.com
Mainly the new sign should display the clinic Chinese and English names, logo, and the phone number. Able to manipulate Chinese characters is a plus.

```html
<!DOCTYPE html>
<html lang="zh-Hant">
<head>
<meta charset="utf-8">
<title>LMT Animal Hospital – Storefront Sign</title>
<link rel="stylesheet" href="https://fonts.googleapis.com/css2?family=Cinzel:wght@700&family=Noto+Sans+TC:wght@400;500&family=Open+Sans:wght@600&display=swap">
<style>
  :root {
    --clinic-red: #c9302c;
    --ink: #161616;
    --sign-white: #f7f7f7;
    --backdrop: #e4e4e2;
  }
  * { box-sizing: border-box; margin: 0; padding: 0; }
  html, body { width: 1200px; height: 900px; overflow: hidden; }
  body { background: var(--backdrop); position: relative; }

  .sign {
    position: absolute; left: 40px; top: 230px;
    width: 1120px; height: 440px;
    background: var(--sign-white);
    overflow: hidden;
    box-shadow: 0 2px 10px rgba(0,0,0,.12);
  }

  .brand-mark {
    position: absolute; left: 70px; top: 70px;
    display: flex; align-items: center; gap: 16px;
  }
  .brand-mark__dot {
    width: 44px; height: 44px; border-radius: 50%;
    background: var(--clinic-red);
  }
  .brand-mark__name {
    font-family: "Cinzel", serif; font-weight: 700;
    font-size: 62px; color: var(--clinic-red); line-height: 1;
  }

  .paw {
    position: absolute; width: 46px; height: 40px; border-radius: 50% 50% 45% 45%;
  }
  .paw--red { background: var(--clinic-red); }
  .paw--black { background: var(--ink); }

  .name-zh {
    position: absolute; left: 420px; top: 34px;
    font-family: "Noto Sans TC", sans-serif; font-weight: 500;
    line-height: 1;
  }
  .name-zh__first {
    display: block; color: var(--clinic-red);
    font-size: 84px; letter-spacing: 26px;
  }
  .name-zh__second {
    display: block; color: var(--ink);
    font-size: 66px; letter-spacing: 22px;
    margin-top: 14px; margin-left: 80px;
  }

  .name-en {
    position: absolute; left: 60px; right: 60px; top: 246px;
    border-top: 3px solid var(--ink);
    border-bottom: 3px solid var(--ink);
    padding: 6px 0 2px;
    text-align: center;
    font-family: "Cinzel", serif; font-weight: 700;
    font-size: 58px; letter-spacing: 4px;
    color: var(--clinic-red); line-height: 1.1;
  }

  .phone-band {
    position: absolute; left: 0; right: 0; bottom: 0; height: 100px;
    background: var(--clinic-red);
    display: flex; align-items: center; justify-content: center; gap: 28px;
  }
  .phone-band__rule {
    flex: 1; height: 4px; background: var(--sign-white);
  }
  .phone-band__rule:first-child { margin-left: 0; }
  .phone-band__text {
    font-family: "Noto Sans TC", "Open Sans", sans-serif; font-weight: 500;
    font-size: 56px; color: var(--sign-white); letter-spacing: 4px;
    white-space: nowrap;
  }
</style>
</head>
<body>
  <section class="sign">
    <div class="paw paw--black" style="left:40px; top:30px;" role="img" aria-label="Paw print ornament"></div>
    <div class="paw paw--red" style="left:20px; top:150px; width:34px; height:30px;" role="img" aria-label="Paw print ornament"></div>
    <div class="paw paw--red" style="left:1010px; top:28px; width:56px; height:48px;" role="img" aria-label="Paw print ornament"></div>
    <div class="paw paw--black" style="left:960px; top:110px;" role="img" aria-label="Paw print ornament"></div>

    <div class="brand-mark">
      <span class="brand-mark__dot"></span>
      <span class="brand-mark__name">LMT</span>
    </div>

    <h1 class="name-zh">
      <span class="name-zh__first">朗明堂動</span>
      <span class="name-zh__second">物醫院</span>
    </h1>

    <p class="name-en">LMT ANIMAL HOSPITAL</p>

    <div class="phone-band">
      <span class="phone-band__rule"></span>
      <span class="phone-band__text">電話: 2388 4155</span>
      <span class="phone-band__rule"></span>
    </div>
  </section>
</body>
</html>
```